Law Firm Business Card

This is a business card for a law firm that serves US military and veterans.

The card must have ONLY the following (we want an uncluttered look):

- Company logo (PNG, GIF, JPEG copies uploaded)
- A tagline reading: "a law firm for service members and veterans"
- My name and title: "Martin Kovel" and "Attorney"
- My email: "mart.kovel@bramblecourtlegal.com"
- My number: "855-MOKE-TIB (665-3842)"

We are looking for a clean, simple layout with only the above information, likely printed on a bright white cotton stock. The font of our logo is DIN 1451, and the font used on our website is Helvetica Neue. The color of our logo is #336699, and we probably want the tagline in that color also, and my contact information in a dark grey. Please review our website at www.bramblecourtlegal.com to ensure your card design complements our website style.

Thanks and we look forward to seeing your submissions.

A few notes:

- Two-sided submissions are ok
- Please don't add graphics (scales of justice, judges hammer, etc)

```html
<!DOCTYPE html>
<html lang="en">
<head>
<meta charset="utf-8">
<title>Bramblecourt Legal – Business Card</title>
<link rel="stylesheet" href="https://fonts.googleapis.com/css2?family=Arimo:wght@400;700&display=swap">
<style>
  :root {
    --brand-blue: #336699;
    --ink-grey: #3a3a3a;
    --card-white: #ffffff;
    --stage: #ececec;
  }
  * { box-sizing: border-box; margin: 0; padding: 0; }
  html, body {
    width: 1200px;
    height: 960px;
    overflow: hidden;
  }
  body {
    background: var(--stage);
    font-family: "Arimo", "Helvetica Neue", Arial, sans-serif;
    position: relative;
  }
  .card {
    position: absolute;
    top: 330px;
    width: 490px;
    height: 280px;
    background: var(--card-white);
    box-shadow: 0 2px 6px rgba(0,0,0,0.12);
    overflow: hidden;
  }
  .card--back { left: 80px; }
  .card--front { left: 630px; }

  /* Back side */
  .tagline {
    position: absolute;
    left: 0; right: 0;
    top: 196px;
    text-align: center;
    color: var(--brand-blue);
    font-size: 17px;
    line-height: 22px;
  }
  .website {
    position: absolute;
    left: 0; right: 0;
    top: 224px;
    text-align: center;
    color: var(--ink-grey);
    font-size: 13px;
    line-height: 18px;
  }

  /* Front side */
  .accent-band {
    position: absolute;
    left: 0; top: 0;
    width: 60px;
    height: 100%;
  }
  .company-name {
    position: absolute;
    right: 40px;
    top: 38px;
    color: var(--brand-blue);
    font-size: 26px;
    line-height: 32px;
    font-weight: 700;
    letter-spacing: 0.5px;
  }
  .contact {
    position: absolute;
    left: 170px;
    top: 148px;
  }
  .contact__name {
    color: var(--brand-blue);
    font-size: 19px;
    line-height: 24px;
  }
  .contact__title {
    color: var(--ink-grey);
    font-size: 16px;
    line-height: 22px;
    margin-top: 2px;
  }
  .contact__list {
    list-style: none;
    margin-top: 16px;
    font-size: 14px;
    line-height: 18px;
    color: var(--ink-grey);
  }
  .contact__list li { margin-bottom: 6px; white-space: nowrap; }
  .contact__label {
    display: inline-block;
    width: 15px;
    color: var(--brand-blue);
    font-weight: 700;
  }
</style>
</head>
<body>
  <section class="card card--back" aria-label="Card back">
    <p class="tagline">a law firm for service members and veterans</p>
    <p class="website">bramblecourtlegal.com</p>
  </section>

  <section class="card card--front" aria-label="Card front">
    <svg class="accent-band" viewBox="0 0 60 280" preserveAspectRatio="none" aria-hidden="true">
      <rect x="0" y="0" width="60" height="280" fill="var(--brand-blue)"/>
    </svg>
    <p class="company-name">Bramblecourt Legal</p>
    <div class="contact">
      <p class="contact__name">Martin Kovel</p>
      <p class="contact__title">Attorney / Owner</p>
      <ul class="contact__list">
        <li><span class="contact__label">e</span> mart.kovel@bramblecourtlegal.com</li>
        <li><span class="contact__label">p</span> 855-MOKE-TIB (665-3842)</li>
      </ul>
    </div>
  </section>
</body>
</html>
```